Sole trader needs a stationery design

We are a sole trader competing in government and tertiary education tenders. We require stationery design to appear more professional than our previous Microsoft standard template.

Our new logo is attached.

Please feel free to add and adjust colours.

Please provide detail on the fonts you are using.

The uploaded font is Tex Gyre Adventor. It is the font of the logo.

Company Details:
Quillon IT

My details are as follows:
Name: Benedict Sallowmere
Role: Front end web consultant
Work: 02 8143 2296
Mobile: 0418 552 306
Address: not required
Email: bsallow@mailvane.net
Website: http://www.quillonit-demo.com.au

Target Market(s)

Government and tertiary institutions

Industry/Entity Type

Information Technology

Font styles to use
Sans Serif

Requirements
Must have
• We require the following stationery design:
• - Business cards
• - Physical letterhead
• - Tender document with coverpage and appendix coverpage
• - Internal tender page
• Content copy items to include:
• - Table
• - Image with caption (figure)
• - Figure text
• - Table of contents
• - Headings (up to 5 levels)
• - Paragraph with bold / italic text
• - Hyperlink
• - Ordered list
• - Bullet list
Should not have
• Serif fonts

```html
<!DOCTYPE html>
<html lang="en">
<head>
<meta charset="utf-8">
<title>Quillon IT – Stationery</title>
<link href="https://fonts.googleapis.com/css2?family=Questrial&display=swap" rel="stylesheet">
<style>
  :root{
    --bg:#d3d3d3;
    --paper:#f7f7f7;
    --slate:#474d57;
    --slate-soft:#545a64;
    --blue:#1a93d6;
    --ink:#3a3f47;
    --muted:#6c717a;
  }
  *{box-sizing:border-box;margin:0;padding:0}
  html,body{width:1200px;height:900px;overflow:hidden}
  body{background:var(--bg);font-family:"Questrial",sans-serif;color:var(--ink);position:relative}
  .sheet{position:absolute;background:var(--paper);box-shadow:0 1px 3px rgba(0,0,0,.18)}
  .wordmark{font-family:"Questrial",sans-serif;color:var(--slate);white-space:nowrap;display:flex;align-items:center;gap:.3em;line-height:1}
  .wordmark .dot{width:.55em;height:.55em;background:var(--blue);display:inline-block}
  .tagline{font-size:4px;color:var(--slate);letter-spacing:.3px;text-transform:uppercase;margin-top:2px}
  .footer-band{position:absolute;left:0;right:0;bottom:0;height:6px;display:flex}
  .footer-band .dark{flex:0 0 68%;background:var(--slate)}
  .footer-band .light{flex:1;background:var(--blue)}

  /* letterhead */
  .letterhead{left:220px;top:54px;width:382px;height:540px}
  .letterhead .wordmark{position:absolute;left:36px;top:34px;font-size:22px}
  .letterhead .tagline{position:absolute;left:36px;top:58px}
  .sender{position:absolute;left:280px;top:30px;font-size:5px;line-height:6.6px}
  .sender .name{font-weight:700;text-transform:uppercase;color:var(--ink);letter-spacing:.2px}
  .sender .role{color:var(--muted);margin-bottom:5px}
  .sender .line{display:flex;align-items:center;gap:3px}
  .sender .icon{width:4px;height:4px;background:var(--blue);display:inline-block}
  .letter{position:absolute;left:36px;top:108px;width:312px;font-size:5.3px;line-height:6.3px;color:var(--ink)}
  .letter p{margin-bottom:6px;text-align:justify}
  .letter .date{margin-bottom:12px}
  .letter .address{margin-bottom:30px}
  .letter .greet{font-weight:700;margin-bottom:7px}
  .letter .close{margin-top:10px}
  .signature{position:absolute;left:90px;top:378px;width:80px;height:40px;background:linear-gradient(90deg,rgba(60,90,180,.12),rgba(60,90,180,.05))}
  .fold-mark{position:absolute;left:0;width:18px;height:1px;background:#d8d8d8}

  /* folder */
  .folder{left:650px;top:40px;width:415px;height:553px;background:var(--slate);border-radius:3px;overflow:hidden}
  .folder .spine{position:absolute;left:22px;top:0;bottom:0;width:1px;background:rgba(0,0,0,.25)}
  .folder .wordmark{position:absolute;left:110px;top:90px;font-size:44px;color:#f2f2f2}
  .folder .wordmark .it{color:var(--blue)}
  .folder .tagline{position:absolute;left:168px;top:132px;font-size:7px;color:#f2f2f2;letter-spacing:.4px}
  .folder .pattern{position:absolute;left:0;right:0;top:200px;bottom:0;background:linear-gradient(180deg,var(--slate) 0%,var(--slate-soft) 55%,var(--slate) 100%)}

  /* business cards */
  .card{width:163px}
  .card-front{left:79px;top:638px;height:89px}
  .card-front .wordmark{position:absolute;left:14px;top:50px;font-size:15px}
  .card-front .tagline{position:absolute;left:14px;top:66px;font-size:3px}
  .card-front .sender{left:96px;top:26px;font-size:3.6px;line-height:5px}
  .card-front .sender .icon{width:3px;height:3px}
  .card-front .footer-band{height:3px}
  .card-back{left:79px;top:747px;height:92px;background:var(--slate)}
  .card-back .wordmark{position:absolute;left:42px;top:38px;font-size:16px;color:#f2f2f2}
  .card-back .tagline{position:absolute;left:66px;top:56px;font-size:3px;color:#f2f2f2}

  /* compliments slip */
  .slip{left:277px;top:639px;width:401px;height:200px}
  .slip .wordmark{position:absolute;left:24px;top:24px;font-size:24px}
  .slip .tagline{position:absolute;left:24px;top:51px}

  /* envelope */
  .envelope{left:724px;top:639px;width:400px;height:200px;overflow:hidden}
  .envelope svg{position:absolute;left:0;top:0}
  .envelope .wordmark{position:absolute;left:0;right:0;top:24px;justify-content:center;font-size:9px;color:#f2f2f2}
</style>
</head>
<body>

<!-- Letterhead -->
<section class="sheet letterhead">
  <div class="wordmark">Quillon IT <span class="dot"></span></div>
  <div class="tagline">Web consulting services</div>
  <div class="sender">
    <div class="name">Benedict Sallowmere</div>
    <div class="role">Front end web consultant</div>
    <div class="line"><span class="icon"></span>02 8143 2296</div>
    <div class="line"><span class="icon"></span>0418 552 306</div>
    <div class="line"><span class="icon"></span>bsallow@mailvane.net</div>
    <div class="line"><span class="icon"></span>www.quillonit-demo.com.au</div>
  </div>
  <span class="fold-mark" style="top:180px"></span>
  <span class="fold-mark" style="top:360px"></span>
  <div class="letter">
    <div class="date">30.02.2015</div>
    <div class="address">Recipient's name<br>Halvenweg 7<br>10719 Velden<br>Germany</div>
    <div class="greet">Dear sir,</div>
    <p>Thank you for the opportunity to respond to your recent request for web services. This letter outlines our approach, timeline and the team we propose for the work.</p>
    <p>We have delivered accessible, standards based websites for councils and universities for over ten years. Each project begins with a short discovery phase, followed by design, build and testing in close contact with your staff.</p>
    <p>Our pricing is fixed for each stage, so there are no surprises. Full details of costs, deliverables and support terms are set out in the attached tender document.</p>
    <p>Please contact me at any time if you have questions. I look forward to working with you.</p>
    <div class="close">Yours Sincerely,<br><strong>Tarin Ollsby</strong></div>
  </div>
  <div class="signature" role="img" aria-label="Handwritten signature"></div>
  <div class="footer-band"><span class="dark"></span><span class="light"></span></div>
</section>

<!-- Presentation folder -->
<section class="sheet folder">
  <span class="spine"></span>
  <div class="wordmark">Quillon IT <span class="dot"></span></div>
  <div class="tagline">Web consulting services</div>
  <div class="pattern" role="img" aria-label="Faint tonal geometric pattern across the lower folder"></div>
</section>

<!-- Business card front -->
<section class="sheet card card-front">
  <div class="wordmark">Quillon IT</div>
  <div class="tagline">Web consulting services</div>
  <div class="sender">
    <div class="name">Benedict Sallowmere</div>
    <div class="role">Front end web consultant</div>
    <div class="line"><span class="icon"></span>02 8143 2296</div>
    <div class="line"><span class="icon"></span>0418 552 306</div>
    <div class="line"><span class="icon"></span>bsallow@mailvane.net</div>
    <div class="line"><span class="icon"></span>www.quillonit-demo.com.au</div>
  </div>
  <div class="footer-band"><span class="dark"></span><span class="light"></span></div>
</section>

<!-- Business card back -->
<section class="sheet card card-back">
  <div class="wordmark">Quillon IT</div>
  <div class="tagline">Web consulting services</div>
</section>

<!-- Compliments slip -->
<section class="sheet slip">
  <div class="wordmark">Quillon IT <span class="dot"></span></div>
  <div class="tagline">Web consulting services</div>
  <div class="footer-band"><span class="dark"></span><span class="light"></span></div>
</section>

<!-- Envelope -->
<section class="sheet envelope">
  <svg width="400" height="200" viewBox="0 0 400 200" aria-hidden="true">
    <polygon points="0,0 400,0 390,30 385,56 15,56 10,30" fill="#474d57"/>
  </svg>
  <div class="wordmark">Quillon IT</div>
</section>

</body>
</html>
```